Dental Design, very professional and noticable

Tindale Ridge Dental Surgery is based in Pelican Waters. We are a fast growing dental surgery and are looking for some professional business cards to send to patients.
We would like to see a design that is Vertical and uses the colours Soft Blue, Silver, White and Black. Maybe a full blue side with moto and details on back? Any other ideas or colours that you may think will make the card look unique is fine.
We need all details on the card that are listed above

Target Market(s)

Families, Retired, Other Professionals and Businesses

Industry/Entity Type

Dental

Contact Information for Business Card

Tindale Ridge Dental Surgery
Family, Cosmetic, Preventative
Dr. Owen Castrey
Dental Surgeon
BDS (Adel) FAE FADI FICD FPFA
phone: (07)50001846
fax: (07)50002917
email: tindaleridgedental@quillpost.com
http://tindaleridgedental.com/

Logo Text

Logo styles of interest
Abstract Logo
Requirements
Must have
• Vertical, Vibrant but Professional, Rounded Edges, Logo on front and back of card (different colours on each side)
Nice to have
• One side completely blue (not sure what shade) with logo and moto on bottom
Other side white, with blue or different coloured logo with details in black and silver?
Logo should show half circle with 1 end as arrow symbolizing pelican waters canal also a magnifine glass also half circled with 1 end as arrow. Any other ideas are welcome.
Should not have
• A tooth. A smile. Toothbrush or Toothpaste. Cornered edges.

```html
<!DOCTYPE html>
<html lang="en">
<head>
<meta charset="utf-8">
<title>Tindale Ridge Dental Surgery – Business Card</title>
<link rel="stylesheet" href="https://fonts.googleapis.com/css2?family=Cabin+Condensed:wght@400;500&family=Noto+Serif:wght@400&display=swap">
<style>
  :root {
    --backdrop: #3a3a3a;
    --navy-edge: #24306a;
    --blue-glow: #0b5a9c;
    --card-white: #ffffff;
    --ink-blue: #1f4f94;
    --gold: #9a7a2c;
    --front-text: #ffffff;
  }
  * { margin: 0; padding: 0; box-sizing: border-box; }
  html, body {
    width: 1200px; height: 900px; overflow: hidden;
    background: var(--backdrop);
  }
  .canvas { position: relative; width: 1200px; height: 900px; }

  .card {
    position: absolute; top: 70px; width: 430px; height: 742px;
    border-radius: 24px; overflow: hidden;
  }
  .card-front {
    left: 113px;
    background: radial-gradient(ellipse 70% 55% at 48% 68%, var(--blue-glow) 0%, #17407f 55%, var(--navy-edge) 100%);
    color: var(--front-text);
    font-family: "Cabin Condensed", sans-serif;
  }
  .card-back {
    left: 655px; width: 428px;
    background: var(--card-white);
    color: var(--ink-blue);
    font-family: "Noto Serif", serif;
    text-align: center;
  }

  .brand-mark {
    position: absolute; left: 50%; transform: translateX(-50%);
    border-radius: 50%;
  }
  .front-mark { top: 338px; width: 44px; height: 44px; background: var(--front-text); }
  .front-name {
    position: absolute; top: 404px; width: 100%; text-align: center;
    font-size: 22px; font-weight: 500; letter-spacing: 0.2px;
  }
  .front-services {
    position: absolute; top: 690px; width: 100%;
    display: flex; justify-content: center; align-items: center; gap: 26px;
    font-size: 18px;
  }
  .front-services .dot { width: 7px; height: 7px; border-radius: 50%; background: var(--front-text); }

  .doctor-name { position: absolute; top: 60px; width: 100%; font-size: 30px; line-height: 1.1; }
  .doctor-role { position: absolute; top: 92px; width: 100%; font-size: 22px; }
  .details { position: absolute; width: 100%; font-size: 20px; line-height: 26px; }
  .credentials { top: 196px; }
  .contact-web { top: 328px; }

  .back-mark { top: 622px; width: 36px; height: 36px; background: var(--gold); }
  .back-name {
    position: absolute; top: 682px; width: 100%;
    font-family: "Cabin Condensed", sans-serif; font-size: 19px; font-weight: 500; color: var(--gold);
  }
  .back-services {
    position: absolute; top: 714px; width: 100%;
    font-size: 13px; color: var(--gold);
  }
</style>
</head>
<body>
<main class="canvas">
  <section class="card card-front">
    <span class="brand-mark front-mark"></span>
    <p class="front-name">Tindale Ridge Dental Surgery</p>
    <p class="front-services">
      <span>Family</span><span class="dot"></span><span>Cosmetic</span><span class="dot"></span><span>Preventive</span>
    </p>
  </section>

  <section class="card card-back">
    <h1 class="doctor-name" style="font-weight:400">Dr. Owen Castrey</h1>
    <p class="doctor-role">Dental Surgeon</p>
    <p class="details credentials">BDS (Adel) FAE FADI FICD FPFA<br>(07)50001846<br>(07)50002917</p>
    <p class="details contact-web">tindaleridgedental@quillpost.com<br>www.tindaleridgedental.com</p>
    <span class="brand-mark back-mark"></span>
    <p class="back-name">Tindale Ridge Dental Surgery</p>
    <p class="back-services">Family, Cosmetic, Preventive</p>
  </section>
</main>
</body>
</html>
```